Flyer-Design für Lumira Afghan Take Away
Zielgruppe
Gastrobetrieb mit Afghanischer Küche. Hauptangebot: Reisgerichte, Teigtaschen und Korma (Currygerichte). ZG: Studenten/Schüller, Ladenbesitzer und Passanten, da es sehr Zentral liegt
Aufgabenstellung
Öffnungszeiten:
MO: 11:30-14h
DI&MI: 11:30-14h/18h-20h
DO&FR: 11:30-14h/18h-21h
SA: 11:30-15h
SO: Geschlossen
INFO: www.lumira-imbiss.ch

```html
<!DOCTYPE html>
<html lang="de">
<head>
<meta charset="utf-8">
<title>Lumira Afghan Take Away – Flyer</title>
<link href="https://fonts.googleapis.com/css2?family=Montserrat:wght@400;600;700;800&display=swap" rel="stylesheet">
<style>
  :root {
    --page-bg: #eef0f1;
    --paper: #ffffff;
    --brand-red: #8e1e1e;
    --accent-red: #d8112b;
    --text-red: #c8102e;
    --forest: #2d5a2a;
    --ink: #1a1a1a;
    --card-top: #ece4d6;
    --card-bottom: #d9b98c;
    --plate: #f4efe6;
  }
  * { box-sizing: border-box; margin: 0; padding: 0; }
  html, body { width: 1200px; height: 1200px; overflow: hidden; }
  body {
    background: var(--page-bg);
    font-family: "Montserrat", Arial, sans-serif;
    color: var(--ink);
    position: relative;
  }
  .flyer {
    position: absolute;
    left: 320px; top: 20px;
    width: 560px; height: 1160px;
    background: var(--paper);
    box-shadow: 0 6px 24px rgba(0,0,0,.12);
    overflow: hidden;
  }
  .top-band {
    position: absolute; left: 0; top: 0;
    width: 100%; height: 34px;
    background: var(--brand-red);
    border-bottom-left-radius: 60% 40%;
  }
  .menu {
    position: absolute; left: 16px; top: 56px;
    width: 384px;
    display: flex; flex-direction: column; gap: 14px;
  }
  .dish {
    position: relative;
    height: 214px;
    border-radius: 8px;
    background: linear-gradient(180deg, var(--card-top) 0%, #e6d6bd 55%, var(--card-bottom) 100%);
    padding: 12px 14px;
    overflow: hidden;
  }
  .dish-name {
    font-weight: 700; font-size: 17px; color: var(--text-red);
  }
  .dish-desc {
    font-size: 11.5px; line-height: 1.3; color: var(--text-red);
    margin-top: 2px; max-width: 340px;
  }
  .dish-photo {
    position: absolute; left: 50%; top: 92px;
    transform: translateX(-50%);
    width: 150px; height: 100px;
    border-radius: 50%;
    background: radial-gradient(ellipse at center, #e7c7a2 0%, #d6a577 45%, var(--plate) 70%);
    box-shadow: 0 4px 10px rgba(0,0,0,.12);
  }
  .price {
    position: absolute; right: 14px; bottom: 14px;
    width: 66px; height: 66px; border-radius: 50%;
    background: var(--accent-red);
    color: #fff; font-weight: 800; font-size: 22px;
    display: flex; align-items: center; justify-content: center;
  }
  .price::before {
    content: ""; position: absolute; left: -8px; top: 6px;
    width: 16px; height: 16px; border-radius: 50%;
    background: var(--accent-red);
  }
  .brand {
    position: absolute; left: 408px; top: 60px;
    width: 140px; text-align: center;
  }
  .brand-mark {
    width: 16px; height: 16px; border-radius: 50%;
    background: var(--brand-red); margin: 0 auto 8px;
  }
  .brand-name {
    font-weight: 800; font-size: 19px; line-height: 1.15;
    color: var(--brand-red); text-transform: uppercase;
  }
  .hours {
    position: absolute; left: 420px; top: 330px;
    height: 600px;
    writing-mode: vertical-rl;
    transform: rotate(180deg);
    font-weight: 700; font-size: 21px; line-height: 1.25;
  }
  .hours-title {
    color: var(--brand-red); text-decoration: underline;
    text-decoration-thickness: 2px;
  }
  .day { color: var(--brand-red); }
  .web { color: var(--forest); }
  .footer-strip {
    position: absolute; left: 0; top: 960px;
    width: 100%; height: 110px;
    display: flex; align-items: center; padding-left: 20px; gap: 24px;
  }
  .footer-brand {
    font-weight: 800; font-size: 15px; line-height: 1.1;
    color: var(--brand-red); text-transform: uppercase; width: 86px;
  }
  .divider {
    width: 0; height: 80px;
    border-left: 3px dotted var(--ink);
  }
  .address {
    display: flex; align-items: flex-start; gap: 12px;
    font-weight: 700; font-size: 26px; line-height: 1.1;
  }
  .address svg { flex: none; margin-top: 2px; }
  .address small { display: block; font-size: 22px; }
  .bottom-band {
    position: absolute; left: 0; bottom: 0;
    width: 100%; height: 90px;
    background: var(--forest);
  }
</style>
</head>
<body>
  <main class="flyer">
    <div class="top-band"></div>

    <section class="menu">
      <article class="dish">
        <h2 class="dish-name">Mantu</h2>
        <p class="dish-desc">Gedämpfte Rindhackfleischtaschen aus frischem Teig, dazu Tomatensauce mit gelben Erbsen und Joghurt-Minze-Sauce</p>
        <div class="dish-photo" role="img" aria-label="Teller mit Mantu, Tomatensauce und Joghurt"></div>
        <div class="price">14.-</div>
      </article>
      <article class="dish">
        <h2 class="dish-name">Ashak</h2>
        <p class="dish-desc">Gedämpfte Lauchtaschen aus frischem Teig, dazu Tomatensauce mit gelben Erbsen und Joghurt-Minze-Sauce</p>
        <div class="dish-photo" role="img" aria-label="Teller mit Ashak und Tomatensauce"></div>
        <div class="price">14.-</div>
      </article>
      <article class="dish">
        <h2 class="dish-name">Chapli-Kabob im Taschenbrot</h2>
        <p class="dish-desc">Gebratene Rindhacksteaks mit Gemüse, Salat, Chili-Koriander und Joghurt-Minze-Sauce</p>
        <div class="dish-photo" role="img" aria-label="Gefülltes Taschenbrot mit Chapli-Kabob"></div>
        <div class="price">9.-</div>
      </article>
      <article class="dish">
        <h2 class="dish-name">Sambosa, 2 Stück</h2>
        <p class="dish-desc">Frittierte Fleisch- oder Gemüsetaschen, dazu Chili-Koriander-Sauce und Joghurt-Minze-Sauce</p>
        <div class="dish-photo" role="img" aria-label="Teller mit Sambosa und zwei Saucen"></div>
        <div class="price">6.-</div>
      </article>
    </section>

    <header class="brand">
      <div class="brand-mark"></div>
      <div class="brand-name">Lumira<br>Afghan<br>Take Away</div>
    </header>

    <section class="hours">
      <div class="hours-title">Öffnungszeiten:</div>
      <div><span class="day">MO:</span> 11:30-14h &nbsp;- &nbsp;<span class="day">DI&amp;MI:</span> 11:30-14h/18h-20h</div>
      <div><span class="day">DO&amp;FR:</span> 11:30-14h/18h-21h</div>
      <div><span class="day">SA:</span> 11:30-15h &nbsp;- &nbsp;<span class="day">SO:</span> Geschlossen</div>
      <div class="web">www.lumira-imbiss.ch</div>
    </section>

    <footer class="footer-strip">
      <div class="footer-brand">Lumira Afghan Take Away</div>
      <div class="divider"></div>
      <div class="address">
        <svg width="22" height="30" viewBox="0 0 22 30" aria-hidden="true">
          <path d="M11 0C4.9 0 0 4.9 0 11c0 8 11 19 11 19s11-11 11-19C22 4.9 17.1 0 11 0z" fill="#1a1a1a"/>
          <circle cx="11" cy="11" r="4.5" fill="#ffffff"/>
        </svg>
        <div>Lindengasse 7<small>8001 Zürich</small></div>
      </div>
    </footer>
    <div class="bottom-band"></div>
  </main>
</body>
</html>
```